I need two seperate flyers made
I have supplied 2 x photos of bathrooms, one for each flyer.
First flyer i want a banner or some sort of blockout acccross the bottom with my business name Marlow Bathrooms and my number 0487650923 and the promo is '' Renovate your bathroom from $10990 and in small writing under neath say owner to supply fixtures and tiles

Second flyer to have the same banner accross bottom and the promo is
Complete bathroom renovations from $15990 with small writing under saying terms and conditions apply

Want these to look professional and eye cathcing to generate more work.

I have attached 2x of our old flyers for reference and our current logo for use
Looking forward to working with you.

```html
<!DOCTYPE html>
<html lang="en">
<head>
<meta charset="utf-8">
<title>Marlow Bathrooms – Renovation Flyers</title>
<link rel="stylesheet" href="https://fonts.googleapis.com/css2?family=Archivo+Black&family=Montserrat:wght@500;600;700&family=Saira+Condensed:wght@600&display=swap">
<style>
  :root {
    --page: #d3d3d3;
    --navy-deep: #0b2a6e;
    --navy-line: #0d3a6a;
    --cyan-accent: #2aa3e6;
    --ice: #93d5e2;
    --frame-white: #ffffff;
    --flyer-base: #f1f2f3;
    --ink: #15233f;
  }
  * { margin: 0; padding: 0; box-sizing: border-box; }
  html, body { width: 796px; height: 1200px; overflow: hidden; background: var(--page); }
  .sheet {
    width: 796px; height: 1200px;
    display: flex; align-items: center; justify-content: center; gap: 20px;
  }
  .flyer {
    display: block; width: 370px; height: 522px;
    background: var(--flyer-base);
    box-shadow: 0 10px 24px rgba(0,0,0,0.35);
  }
  .brand-name { font-family: "Montserrat", sans-serif; font-weight: 600; font-size: 27px; letter-spacing: 1px; fill: var(--ink); }
  .brand-sub { font-family: "Montserrat", sans-serif; font-weight: 600; font-size: 10px; letter-spacing: 5px; fill: var(--ink); }
  .promo-title { font-family: "Archivo Black", sans-serif; font-size: 37px; letter-spacing: 0.5px; fill: #fff; }
  .promo-from { font-family: "Montserrat", sans-serif; font-weight: 600; font-size: 22px; fill: var(--ice); }
  .promo-amount { font-family: "Saira Condensed", sans-serif; font-weight: 600; font-size: 36px; fill: var(--ice); }
  .promo-note { font-family: "Montserrat", sans-serif; font-weight: 500; font-size: 15px; fill: var(--ink); }
  .promo-phone { font-family: "Montserrat", sans-serif; font-weight: 700; font-size: 16px; fill: #fff; }
</style>
</head>
<body>
<main class="sheet">

  <!-- flyer: complete renovations -->
  <svg class="flyer" viewBox="0 0 583 823" width="370" height="522" aria-label="Flyer from $15990">
    <defs>
      <linearGradient id="a-banner" x1="0" y1="0" x2="1" y2="1">
        <stop offset="0" stop-color="#0d2f7a"/><stop offset="1" stop-color="#0f5cb5"/>
      </linearGradient>
      <linearGradient id="a-hero" x1="0" y1="0" x2="0" y2="1">
        <stop offset="0" stop-color="#e9e7e3"/><stop offset="0.6" stop-color="#d8d3cc"/><stop offset="1" stop-color="#c3bdb4"/>
      </linearGradient>
      <linearGradient id="a-left" x1="0" y1="0" x2="1" y2="1">
        <stop offset="0" stop-color="#b3ab8c"/><stop offset="1" stop-color="#8c866f"/>
      </linearGradient>
      <linearGradient id="a-centre" x1="0" y1="0" x2="0" y2="1">
        <stop offset="0" stop-color="#e3e4e4"/><stop offset="1" stop-color="#a27a5b"/>
      </linearGradient>
      <linearGradient id="a-right" x1="0" y1="0" x2="1" y2="1">
        <stop offset="0" stop-color="#c2cac5"/><stop offset="1" stop-color="#e8e4df"/>
      </linearGradient>
    </defs>
    <polygon points="0,0 583,0 583,224 291,457 0,224" fill="url(#a-hero)" role="img" aria-label="Photo of a renovated bathroom with white vanity, vessel basin and pill-shaped mirror"/>
    <polyline points="0,224 291,457 583,224" fill="none" stroke="var(--navy-line)" stroke-width="8"/>
    <polygon points="0,606 291,370 583,606 583,823 0,823" fill="var(--cyan-accent)"/>
    <polygon points="0,626 291,390 583,626 583,823 0,823" fill="url(#a-banner)"/>
    <rect x="0" y="819" width="583" height="4" fill="var(--cyan-accent)"/>

    <polygon points="291,270 448,427 291,584 134,427" fill="var(--frame-white)"/>
    <polygon points="291,282 436,427 291,572 146,427" fill="url(#a-centre)" role="img" aria-label="Photo of a timber wall-hung vanity with black basin"/>
    <polygon points="110,323 213,426 110,529 7,426" fill="var(--ice)"/>
    <polygon points="110,331 205,426 110,521 15,426" fill="url(#a-left)" role="img" aria-label="Photo of a shower with green tiles and black rail"/>
    <polygon points="472,323 575,426 472,529 369,426" fill="var(--ice)"/>
    <polygon points="472,331 567,426 472,521 377,426" fill="url(#a-right)" role="img" aria-label="Photo of a freestanding bath beside a window"/>

    <text class="brand-name" x="291" y="95" text-anchor="middle">MARLOW</text>
    <text class="brand-sub" x="294" y="114" text-anchor="middle">BATHROOMS</text>

    <text class="promo-title" x="291" y="639" text-anchor="middle">RENOVATE YOUR</text>
    <text class="promo-title" x="291" y="680" text-anchor="middle">BATHROOM</text>
    <rect x="176" y="690" width="230" height="2" fill="var(--ice)"/>
    <text x="291" y="733" text-anchor="middle"><tspan class="promo-from">from </tspan><tspan class="promo-amount">$15990</tspan></text>
    <rect x="116" y="752" width="342" height="24" rx="12" fill="var(--ice)"/>
    <text class="promo-note" x="287" y="769" text-anchor="middle">Terms and conditions apply</text>
    <path transform="translate(226,789) scale(0.72)" fill="#fff" d="M6.6 10.8a15.1 15.1 0 0 0 6.6 6.6l2.2-2.2a1 1 0 0 1 1-.25 11.4 11.4 0 0 0 3.6.57 1 1 0 0 1 1 1V20a1 1 0 0 1-1 1A17 17 0 0 1 3 4a1 1 0 0 1 1-1h3.5a1 1 0 0 1 1 1c0 1.25.2 2.45.57 3.57a1 1 0 0 1-.25 1z"/>
    <text class="promo-phone" x="300" y="803" text-anchor="middle">0487650923</text>
  </svg>

  <!-- flyer: renovate your bathroom -->
  <svg class="flyer" viewBox="0 0 583 823" width="370" height="522" aria-label="Flyer from $10990">
    <defs>
      <linearGradient id="b-banner" x1="0" y1="0" x2="1" y2="1">
        <stop offset="0" stop-color="#0d2f7a"/><stop offset="1" stop-color="#0f5cb5"/>
      </linearGradient>
      <linearGradient id="b-hero" x1="0" y1="0" x2="1" y2="1">
        <stop offset="0" stop-color="#a9adae"/><stop offset="0.5" stop-color="#d9dcdc"/><stop offset="1" stop-color="#c7cacb"/>
      </linearGradient>
      <linearGradient id="b-left" x1="0" y1="0" x2="0" y2="1">
        <stop offset="0" stop-color="#b9b4ad"/><stop offset="1" stop-color="#2c3034"/>
      </linearGradient>
      <linearGradient id="b-centre" x1="0" y1="0" x2="0" y2="1">
        <stop offset="0" stop-color="#b8b9bb"/><stop offset="1" stop-color="#ebebeb"/>
      </linearGradient>
      <linearGradient id="b-right" x1="0" y1="0" x2="1" y2="1">
        <stop offset="0" stop-color="#c4c8cb"/><stop offset="1" stop-color="#e6e7e8"/>
      </linearGradient>
    </defs>
    <polygon points="0,0 583,0 583,224 291,457 0,224" fill="url(#b-hero)" role="img" aria-label="Photo of a bathroom with herringbone tiles, backlit round mirror and white vanity"/>
    <polyline points="0,224 291,457 583,224" fill="none" stroke="var(--navy-line)" stroke-width="8"/>
    <polygon points="0,606 291,370 583,606 583,823 0,823" fill="var(--cyan-accent)"/>
    <polygon points="0,626 291,390 583,626 583,823 0,823" fill="url(#b-banner)"/>
    <rect x="0" y="819" width="583" height="4" fill="var(--cyan-accent)"/>

    <polygon points="291,270 448,427 291,584 134,427" fill="var(--frame-white)"/>
    <polygon points="291,282 436,427 291,572 146,427" fill="url(#b-centre)" role="img" aria-label="Photo of a round vessel basin with black tapware"/>
    <polygon points="110,323 213,426 110,529 7,426" fill="var(--ice)"/>
    <polygon points="110,331 205,426 110,521 15,426" fill="url(#b-left)" role="img" aria-label="Photo of a dark vanity under a wall mirror"/>
    <polygon points="472,323 575,426 472,529 369,426" fill="var(--ice)"/>
    <polygon points="472,331 567,426 472,521 377,426" fill="url(#b-right)" role="img" aria-label="Photo of a small basin beside a window"/>

    <text class="brand-name" x="291" y="95" text-anchor="middle">MARLOW</text>
    <text class="brand-sub" x="294" y="114" text-anchor="middle">BATHROOMS</text>

    <text class="promo-title" x="291" y="639" text-anchor="middle">RENOVATE YOUR</text>
    <text class="promo-title" x="291" y="680" text-anchor="middle">BATHROOM</text>
    <rect x="176" y="690" width="230" height="2" fill="var(--ice)"/>
    <text x="291" y="733" text-anchor="middle"><tspan class="promo-from">from </tspan><tspan class="promo-amount">$10990</tspan></text>
    <rect x="116" y="752" width="342" height="24" rx="12" fill="var(--ice)"/>
    <text class="promo-note" x="287" y="769" text-anchor="middle">Owner to supply fixtures and tiles</text>
    <path transform="translate(226,789) scale(0.72)" fill="#fff" d="M6.6 10.8a15.1 15.1 0 0 0 6.6 6.6l2.2-2.2a1 1 0 0 1 1-.25 11.4 11.4 0 0 0 3.6.57 1 1 0 0 1 1 1V20a1 1 0 0 1-1 1A17 17 0 0 1 3 4a1 1 0 0 1 1-1h3.5a1 1 0 0 1 1 1c0 1.25.2 2.45.57 3.57a1 1 0 0 1-.25 1z"/>
    <text class="promo-phone" x="300" y="803" text-anchor="middle">0487650923</text>
  </svg>

</main>
</body>
</html>
```